Brightpath Consulting WA Business Card

Create an interesting, eye catching and colourful two sided business card. We are a business consulting operation assisting SME's improve all areas of their business. We provide consulting services to assist SME's to create a culture of continuous improvement, making a positive difference in the business. Our tag line is Small changes, big rewards. We want to create a well recognised, innovative brand that can be continued throughout our website, social media and email correspondence.

Target Market(s)

Small to Medium Enterprise Business Owners

Industry/Entity Type

Business Consultant

Contact Information for Business Card

Name of Business: Brightpath Consulting - Small Changes Big Rewards
Dean Morrow Ph 0407358164 Lydia Morrow Ph 0409583417
Email brightpathconsultingwa@examplemail.com
Web address TBA
FaceBook page TBA

BACKSIDE OF CARD

Providing assistance with:

• Organisation & Efficiency
• Revenue generation & Marketing
• Financial Management
• Production quality & delivery
• Systems & Process documentation
• Exit Strategy

Font styles to use
Other font styles liked:
• Calibri

Colors

Designer to choose colors to be used in the design.

Requirements
Must have
• Calibri font

```html
<!DOCTYPE html>
<html lang="en">
<head>
<meta charset="utf-8">
<title>Brightpath Consulting WA – Business Card</title>
<link rel="stylesheet" href="https://fonts.googleapis.com/css2?family=Carlito:ital,wght@0,400;0,700;1,400;1,700&display=swap">
<style>
  :root {
    --stage: #2a2d31;
    --card-dark: #0d0d0d;
    --pattern-dark: #1f1f1f;
    --card-light: #ffffff;
    --brand-red: #e8432f;
    --band-yellow-start: #f6a623;
    --band-yellow-end: #ffe14a;
    --band-green-start: #cde13a;
    --band-green-end: #6cb42c;
    --corner-yellow: #f7c418;
    --corner-green: #76b82a;
    --corner-blue: #2f8fd0;
    --corner-red: #e5432e;
    --ink: #111111;
    --ink-soft: #3a3a3a;
    --text-light: #f2f2f2;
    --text-muted: #bdbdbd;
  }
  * { box-sizing: border-box; margin: 0; padding: 0; }
  html, body { width: 1200px; height: 900px; overflow: hidden; }
  body {
    background: var(--stage);
    font-family: "Carlito", "Calibri", sans-serif;
    display: flex;
    align-items: center;
    justify-content: center;
    gap: 60px;
  }
  .card {
    position: relative;
    width: 540px;
    height: 320px;
    border-radius: 24px;
    overflow: hidden;
    box-shadow: 0 14px 30px rgba(0,0,0,.45);
  }

  /* Front */
  .card-front { background: var(--card-dark); color: var(--text-light); }
  .front-pattern {
    position: absolute;
    left: 150px; top: -20px;
    width: 320px; height: 360px;
    border-radius: 60px;
    background: radial-gradient(ellipse at center, #262626 0%, var(--pattern-dark) 60%, var(--card-dark) 100%);
  }
  .brand {
    position: absolute;
    top: 46px; left: 0; right: 0;
    text-align: center;
  }
  .brand-name {
    display: inline-flex;
    align-items: center;
    gap: 12px;
    font-size: 34px;
    font-weight: 700;
    color: var(--brand-red);
    line-height: 1;
  }
  .brand-mark {
    width: 30px; height: 30px;
    border-radius: 6px;
    background: var(--corner-blue);
  }
  .brand-tagline {
    margin-top: 6px;
    font-size: 17px;
    font-style: italic;
    color: var(--text-muted);
  }
  .contact-band {
    position: absolute;
    top: 140px; left: 0; right: 0;
    height: 74px;
    display: flex;
  }
  .band-half {
    flex: 1;
    display: flex;
    flex-direction: column;
    justify-content: center;
    color: var(--ink);
  }
  .band-left {
    background: linear-gradient(90deg, var(--band-yellow-start), var(--band-yellow-end));
    padding-left: 46px;
  }
  .band-right {
    background: linear-gradient(90deg, var(--band-green-start), var(--band-green-end));
    align-items: flex-end;
    padding-right: 46px;
  }
  .person-name { font-size: 24px; font-weight: 700; line-height: 1.05; }
  .person-phone {
    display: flex; align-items: center; gap: 6px;
    font-size: 20px; line-height: 1.1;
  }
  .band-right .person-phone { flex-direction: row-reverse; }
  .phone-icon { width: 18px; height: 18px; fill: var(--ink); }
  .band-divider {
    position: absolute;
    left: 50%; top: 50%;
    width: 30px; height: 30px;
    transform: translate(-50%, -50%);
    border-radius: 50%;
    background: var(--brand-red);
    border: 3px solid var(--card-dark);
  }
  .web-details {
    position: absolute;
    top: 232px; left: 0; right: 0;
    text-align: center;
    font-size: 16px;
    line-height: 1.45;
    color: var(--text-light);
  }

  /* Back */
  .card-back { background: var(--card-light); }
  .corner {
    position: absolute;
    width: 54px; height: 54px;
  }
  .corner-tl { top: 0; left: 0; background: var(--corner-yellow); border-bottom-right-radius: 54px; }
  .corner-tr { top: 0; right: 0; background: var(--corner-blue); border-bottom-left-radius: 54px; }
  .corner-bl { bottom: 0; left: 0; background: var(--corner-green); border-top-right-radius: 54px; }
  .corner-br { bottom: 0; right: 0; background: var(--corner-red); border-top-left-radius: 54px; }
  .services {
    position: absolute;
    top: 44px; left: 0; right: 0;
    text-align: center;
  }
  .services-title {
    font-size: 24px;
    font-weight: 700;
    font-style: italic;
    color: var(--brand-red);
  }
  .services-rule {
    width: 290px;
    height: 2px;
    margin: 12px auto 22px;
    background: var(--ink);
  }
  .services-list {
    list-style: none;
    font-size: 18px;
    line-height: 1.3;
    color: var(--ink-soft);
  }
  .services-list li::before { content: "• "; }
</style>
</head>
<body>

  <section class="card card-front" aria-label="Business card front">
    <div class="front-pattern" role="img" aria-label="Subtle dark interlocking background motif"></div>

    <div class="brand">
      <div class="brand-name"><span>Brightpath Consulting</span><span class="brand-mark"></span></div>
      <div class="brand-tagline">Small Changes, Big Rewards</div>
    </div>

    <div class="contact-band">
      <div class="band-half band-left">
        <div class="person-name">Dean Morrow</div>
        <div class="person-phone">
          <svg class="phone-icon" viewBox="0 0 24 24" aria-hidden="true"><path d="M6.6 10.8a15.1 15.1 0 0 0 6.6 6.6l2.2-2.2a1 1 0 0 1 1-.25 11.4 11.4 0 0 0 3.6.57 1 1 0 0 1 1 1V20a1 1 0 0 1-1 1A17 17 0 0 1 3 4a1 1 0 0 1 1-1h3.5a1 1 0 0 1 1 1c0 1.25.2 2.45.57 3.57a1 1 0 0 1-.25 1z"/></svg>
          <span>040 735 8164</span>
        </div>
      </div>
      <div class="band-half band-right">
        <div class="person-name">Lydia Morrow</div>
        <div class="person-phone">
          <svg class="phone-icon" viewBox="0 0 24 24" aria-hidden="true"><path d="M6.6 10.8a15.1 15.1 0 0 0 6.6 6.6l2.2-2.2a1 1 0 0 1 1-.25 11.4 11.4 0 0 0 3.6.57 1 1 0 0 1 1 1V20a1 1 0 0 1-1 1A17 17 0 0 1 3 4a1 1 0 0 1 1-1h3.5a1 1 0 0 1 1 1c0 1.25.2 2.45.57 3.57a1 1 0 0 1-.25 1z"/></svg>
          <span>040 958 3417</span>
        </div>
      </div>
      <span class="band-divider"></span>
    </div>

    <div class="web-details">
      <div>facebookaddresshere</div>
      <div>brightpathconsultingwa@examplemail.com / www.websitehere.com</div>
    </div>
  </section>

  <section class="card card-back" aria-label="Business card back">
    <span class="corner corner-tl"></span>
    <span class="corner corner-tr"></span>
    <span class="corner corner-bl"></span>
    <span class="corner corner-br"></span>

    <div class="services">
      <h2 class="services-title">Providing assistance with</h2>
      <div class="services-rule"></div>
      <ul class="services-list">
        <li>Organisation &amp; Efficiency</li>
        <li>Revenue generation &amp; Marketing</li>
        <li>Financial Management</li>
        <li>Production quality &amp; delivery</li>
        <li>Systems &amp; Process documentation</li>
        <li>Exit Strategy</li>
      </ul>
    </div>
  </section>

</body>
</html>
```